Sol Rumbo Coaching Services

My info is
Darsie Quenell-Abaro
darsie@solrumbocoaching.example
solrumbocoaching.example
555-413-7082

you can play with order of items. I've never had a letterhead before. Thank you!

```html
<!DOCTYPE html>
<html lang="en">
<head>
<meta charset="utf-8">
<title>Sol Rumbo Coaching Services — Letterhead</title>
<link rel="stylesheet" href="https://fonts.googleapis.com/css2?family=Montserrat:wght@500&family=Roboto+Condensed:wght@300;400;700&family=Open+Sans:wght@400&display=swap">
<style>
  :root {
    --backdrop: #363636;
    --paper: #ffffff;
    --brand-orange: #f7941d;
    --brand-red: #be1e2d;
    --ink: #1a1a1a;
    --rule: #8a8a8a;
    --ghost: #ebebeb;
    --ghost-ring: #e2e2e2;
  }
  * { margin: 0; padding: 0; box-sizing: border-box; }
  html, body {
    width: 879px; height: 1200px; overflow: hidden;
    background: var(--backdrop);
  }
  .letterhead {
    position: absolute; left: 88px; top: 138px;
    width: 696px; height: 961px;
    background: var(--paper);
    overflow: hidden;
  }
  .brand {
    position: absolute; left: 70px; top: 26px; width: 288px;
    display: flex; flex-direction: column; align-items: center;
  }
  .brand-mark {
    width: 98px; height: 98px; border-radius: 50%;
    background: var(--brand-orange);
    box-shadow: 0 0 0 3px var(--paper), 0 0 0 4.5px var(--brand-red);
  }
  .brand-name {
    margin-top: 18px;
    font-family: "Montserrat", sans-serif; font-weight: 500;
    color: var(--brand-red);
    text-align: center; text-transform: uppercase;
    letter-spacing: 4px; line-height: 1.35;
  }
  .brand-name .line-main { display: block; font-size: 30px; letter-spacing: 3px; }
  .brand-name .line-sub { display: block; font-size: 17px; }
  .contact-panel {
    position: absolute; left: 394px; top: 68px;
    width: 302px; height: 134px;
    background: var(--brand-orange);
    display: flex; flex-direction: column; align-items: center; justify-content: center;
    font-family: "Roboto Condensed", sans-serif;
    padding-top: 4px;
  }
  .contact-name { color: var(--paper); font-weight: 300; font-size: 27px; line-height: 1.1; }
  .contact-phone { color: var(--ink); font-weight: 400; font-size: 19px; margin-top: 2px; }
  .date-field {
    position: absolute; left: 394px; top: 219px;
    display: flex; align-items: flex-end;
  }
  .date-label {
    background: var(--brand-red); color: var(--paper);
    font-family: "Roboto Condensed", sans-serif; font-weight: 700;
    font-size: 16px; line-height: 20px; padding: 0 6px; height: 20px;
  }
  .date-line {
    width: 228px; height: 0; margin-left: 7px; margin-bottom: 3px;
    border-top: 1.5px solid var(--rule);
  }
  .ghost-brand {
    position: absolute; left: 0; right: 0; top: 423px;
    display: flex; flex-direction: column; align-items: center;
  }
  .ghost-mark {
    width: 136px; height: 136px; border-radius: 50%;
    background: #f3f2f2;
    box-shadow: 0 0 0 4px var(--paper), 0 0 0 6px var(--ghost-ring);
  }
  .ghost-name {
    margin-top: 30px;
    font-family: "Montserrat", sans-serif; font-weight: 500;
    color: var(--ghost); text-transform: uppercase;
    text-align: center; line-height: 1.3;
  }
  .ghost-name .line-main { display: block; font-size: 58px; letter-spacing: 4px; }
  .ghost-name .line-sub { display: block; font-size: 26px; letter-spacing: 6px; }
  .footer-band {
    position: absolute; left: 0; bottom: 0; width: 100%; height: 31px;
    background: var(--brand-red);
    display: flex; align-items: center; justify-content: center;
    font-family: "Open Sans", sans-serif; font-size: 14px; color: var(--paper);
    letter-spacing: 0.3px;
  }
  .footer-band .divider { margin: 0 8px; }
</style>
</head>
<body>
  <main class="letterhead">
    <header>
      <div class="brand">
        <div class="brand-mark"></div>
        <div class="brand-name">
          <span class="line-main">Sol Rumbo</span>
          <span class="line-sub">Coaching Services</span>
        </div>
      </div>
      <div class="contact-panel">
        <p class="contact-name">Darsie Quenell-Abaro</p>
        <p class="contact-phone">REACH US: 555-413-7082</p>
      </div>
      <div class="date-field">
        <span class="date-label">DATE :</span>
        <span class="date-line"></span>
      </div>
    </header>

    <div class="ghost-brand" aria-hidden="true">
      <div class="ghost-mark"></div>
      <div class="ghost-name">
        <span class="line-main">Sol Rumbo</span>
        <span class="line-sub">Coaching Services</span>
      </div>
    </div>

    <footer class="footer-band">
      <span>darsie@solrumbocoaching.example</span>
      <span class="divider">|</span>
      <span>solrumbocoaching.example</span>
    </footer>
  </main>
</body>
</html>
```